Zielgruppe
Wir sind ein IT Systemhaus mit einem Scherpunkt auf Wireless LAN für Gewerbekunden
https://www.quarvelo-netz.de/wlan-beratung/
Aufgabenstellung
Im Anhang finden Sie einige Stichpunkte/Texte und eine PPT mit Grafiken, sowie unser Briefpapier.
Ziel ist es 1 Flyer A4 Einseitig zu erhalten – Wir benötigen diesen As soon as possible
Das Thema lautet hier:
1. Lernoffensive Klassen
Grafiken können Sie aus der PPT oder der Webseite entnehmen
Die Flyer sollten im oberen Bereich wie unser Briefpapier aussehen und Farbmäßig unserem CD entsprechen
#1e73be
Den Orangeton finde ich leider gerade nicht ☹
An Ergänzenden Grafiken sind wir ebenfalls Interessiert.
Die Welle haben wir leider nicht als Vectorgrafik

```html
<!DOCTYPE html>
<html lang="de">
<head>
<meta charset="utf-8">
<title>Quarvelo Flyer – WLAN & Lernoffensive Klassen</title>
<link href="https://fonts.googleapis.com/css2?family=Roboto:ital,wght@0,400;0,500;1,300;1,400;1,500;1,700&display=swap" rel="stylesheet">
<style>
  :root{
    --brand-blue:#1e73be;
    --wave-mid:#4b9fd9;
    --wave-light:#bddcf2;
    --ink:#4a4a4a;
    --ink-soft:#555555;
    --accent-orange:#f07d1a;
    --backdrop:#9a9a9a;
    --paper:#ffffff;
  }
  *{margin:0;padding:0;box-sizing:border-box}
  html,body{width:1200px;height:823px;overflow:hidden;background:var(--backdrop)}
  body{position:relative;font-family:"Roboto",Arial,sans-serif;color:var(--ink)}

  .flyer{position:absolute;top:9px;width:570px;height:805px;background:var(--paper);overflow:hidden;box-shadow:0 0 4px rgba(0,0,0,.25)}
  .flyer--wlan{left:12px}
  .flyer--school{left:621px}

  .wave-top{position:absolute;left:0;top:0;width:570px;height:92px}
  .wave-bottom{position:absolute;left:0;top:700px;width:570px;height:105px;z-index:2}
  .photo{position:absolute;left:0;top:420px;width:570px;height:385px;z-index:1}

  .brand{position:absolute;right:34px;top:46px;font-size:30px;font-weight:400;letter-spacing:2px;color:#5a5a5a;line-height:1}

  .flyer__title{position:absolute;left:24px;top:122px;font-size:29px;font-style:italic;font-weight:500;color:var(--brand-blue);letter-spacing:.2px;white-space:nowrap}

  .section{position:absolute;left:24px;width:290px}
  .section__heading{font-size:13.5px;font-style:italic;font-weight:500;color:var(--ink);margin-bottom:8px}
  .section__list{list-style:none}
  .section__list li{position:relative;padding-left:17px;font-size:12.3px;font-style:italic;font-weight:400;line-height:18.5px;color:var(--ink-soft)}
  .section__list li::before{content:"•";position:absolute;left:3px;font-size:9px;color:#888}

  .service{position:absolute;left:360px;display:flex;align-items:center;gap:17px}
  .service__icon{width:54px;height:54px;border:1.3px solid var(--brand-blue);border-radius:9px;display:flex;align-items:center;justify-content:center}
  .service__icon svg{width:36px;height:36px}
  .service__label{font-size:13px;font-style:italic;font-weight:500;color:var(--brand-blue);line-height:16px}

  .benefits{position:absolute;left:16px;width:231px;background:var(--brand-blue);color:#fff;padding:18px 30px 0 18px;z-index:3}
  .benefits__heading{font-size:13.5px;font-style:italic;font-weight:500;margin-bottom:10px}
  .benefits__list{list-style:none}
  .benefits__list li{position:relative;padding-left:10px;font-size:10.8px;font-style:italic;font-weight:400;line-height:13.8px;margin-bottom:14px}
  .benefits__list li::before{content:"•";position:absolute;left:0;font-size:8px}

  .contact{position:absolute;right:12px;bottom:9px;z-index:4;color:#fff;font-size:12px;font-style:italic;font-weight:500}
</style>
</head>
<body>

<article class="flyer flyer--wlan">
  <svg class="wave-top" viewBox="0 0 570 92" preserveAspectRatio="none">
    <path d="M0 0H570V12C430 30 250 14 0 28Z" fill="var(--brand-blue)"/>
    <path d="M0 28C250 14 430 30 570 12V30C420 56 250 30 0 60Z" fill="var(--wave-mid)"/>
    <path d="M0 60C250 30 420 56 570 30V42C420 72 260 50 0 90Z" fill="var(--wave-light)"/>
  </svg>

  <div class="brand">QUARVELO</div>

  <h1 class="flyer__title">WLAN für Bauunternehmen &amp; Elektriker</h1>

  <section class="section" style="top:166px">
    <h2 class="section__heading">Mehrwerte für Ihr Unternehmen:</h2>
    <ul class="section__list">
      <li>Alleinstellungsmarkmal gegenüber Mitbewerbern</li>
      <li>Schaffung neuer (monetärer) Mehrwerte</li>
      <li>Risikominderung für WLAN Fehlplanungen</li>
    </ul>
  </section>

  <section class="section" style="top:262px;width:280px">
    <h2 class="section__heading">Mehrwerte für Ihre Kunden:</h2>
    <ul class="section__list">
      <li>Professionelles WLAN bereits beim Einzug</li>
      <li>WLAN nach Stand der Technik</li>
      <li>Investitionskosten für WLAN bereits im<br>Rahmen der Gebäudefinanzierung planbar</li>
      <li>Investitionskosten über Gebäudefinazierung<br>planbar</li>
    </ul>
  </section>

  <section class="section" style="top:413px;width:270px">
    <h2 class="section__heading">Die Quarvelo GmbH bietet:</h2>
    <ul class="section__list">
      <li>Erfahrung mit Bauvorhaben in privaten<br>und öffentlichen Bereichen</li>
      <li>ISO 9001 und ISO 27001 zertifiziert</li>
      <li>Professionelle WLAN-Beratung<br>von Konzept bis zur<br>Konfiguration</li>
    </ul>
  </section>

  <div class="service" style="top:221px">
    <div class="service__icon">
      <svg viewBox="0 0 36 36"><rect x="3" y="5" width="24" height="24" fill="none" stroke="var(--accent-orange)" stroke-width="2.2"/><path d="M8 10H22V24M8 10V24H16M13 16H20" fill="none" stroke="var(--accent-orange)" stroke-width="1.6"/><g fill="none" stroke="var(--brand-blue)" stroke-width="1.6"><path d="M24 27a6 6 0 0 1 8 0"/><path d="M22 24a9 9 0 0 1 12 0"/></g><circle cx="28" cy="30" r="1.5" fill="var(--brand-blue)"/></svg>
    </div>
    <div class="service__label">WLAN Planung</div>
  </div>

  <div class="service" style="top:290px">
    <div class="service__icon">
      <svg viewBox="0 0 36 36"><path d="M4 17L18 5L32 17M8 14V31H22" fill="none" stroke="var(--accent-orange)" stroke-width="2.4"/><circle cx="17" cy="20" r="2" fill="var(--accent-orange)"/><g fill="none" stroke="var(--accent-orange)" stroke-width="1.5"><path d="M13 16a6 6 0 0 0 0 8M21 16a6 6 0 0 1 0 8"/></g><g fill="none" stroke="var(--brand-blue)" stroke-width="1.6"><path d="M25 29a5 5 0 0 1 7 0"/><path d="M23 26a8 8 0 0 1 11 0"/></g><circle cx="28.5" cy="32" r="1.5" fill="var(--brand-blue)"/></svg>
    </div>
    <div class="service__label">WLAN<br>Ausleuchtung</div>
  </div>

  <div class="service" style="top:360px">
    <div class="service__icon">
      <svg viewBox="0 0 36 36"><rect x="6" y="4" width="18" height="28" fill="var(--accent-orange)"/><g fill="#fff"><rect x="9" y="8" width="4" height="4"/><rect x="17" y="8" width="4" height="4"/><rect x="9" y="15" width="4" height="4"/><rect x="17" y="15" width="4" height="4"/><rect x="9" y="22" width="4" height="4"/></g><g fill="none" stroke="var(--brand-blue)" stroke-width="1.6"><path d="M25 29a5 5 0 0 1 7 0"/><path d="M23 26a8 8 0 0 1 11 0"/></g><circle cx="28.5" cy="32" r="1.5" fill="var(--brand-blue)"/></svg>
    </div>
    <div class="service__label">WLAN<br>Infrastruktur</div>
  </div>

  <svg class="photo" viewBox="0 0 570 385" role="img" aria-label="Foto: Hände über Bauplänen mit Lineal und Bleistift">
    <defs>
      <linearGradient id="blueprintTones" x1="0" y1="0" x2="1" y2="1">
        <stop offset="0" stop-color="#ece9e4"/>
        <stop offset=".5" stop-color="#d9d3cb"/>
        <stop offset="1" stop-color="#c4b4a4"/>
      </linearGradient>
    </defs>
    <path d="M150 160C300 110 430 60 570 28V385H150Z" fill="url(#blueprintTones)"/>
  </svg>

  <svg class="wave-bottom" viewBox="0 0 570 105" preserveAspectRatio="none">
    <path d="M0 105C200 90 380 50 570 12V105Z" fill="var(--wave-light)"/>
    <path d="M120 105C300 88 450 58 570 40V105Z" fill="var(--wave-mid)"/>
    <path d="M260 105C400 92 500 78 570 68V105Z" fill="var(--brand-blue)"/>
  </svg>

  <aside class="benefits" style="top:591px;height:204px">
    <h3 class="benefits__heading">Ihre Vorteile auf einen Blick:</h3>
    <ul class="benefits__list">
      <li>Planung und Ausleuchtung vom Profi</li>
      <li>Konfiguration und Montage durch zertifizierte Techniker</li>
      <li>Kompetente und objektive Beratung vom Fachmann</li>
      <li>Maximale Effizienz und kalkulierbare Kosten</li>
    </ul>
  </aside>

  <div class="contact">info@quarvelo-netz.de | www.quarvelo-netz.de</div>
</article>

<article class="flyer flyer--school">
  <svg class="wave-top" viewBox="0 0 570 92" preserveAspectRatio="none">
    <path d="M0 0H570V12C430 30 250 14 0 28Z" fill="var(--brand-blue)"/>
    <path d="M0 28C250 14 430 30 570 12V30C420 56 250 30 0 60Z" fill="var(--wave-mid)"/>
    <path d="M0 60C250 30 420 56 570 30V42C420 72 260 50 0 90Z" fill="var(--wave-light)"/>
  </svg>

  <div class="brand">QUARVELO</div>

  <h1 class="flyer__title" style="top:113px">Lernoffensive Klassen</h1>

  <section class="section" style="top:166px">
    <h2 class="section__heading">Mehrwert für die Schule:</h2>
    <ul class="section__list">
      <li>90% der Kosten werden vom Staat übernommen</li>
      <li>Reputationsvorteil durch digitales Lernangebot</li>
      <li>Moderne Unterrichtsmethoden</li>
    </ul>
  </section>

  <section class="section" style="top:278px">
    <h2 class="section__heading">Mehrwert für die Schüler:</h2>
    <ul class="section__list">
      <li>Routinierter Umgang mit modernen Medien</li>
      <li>Verbesserte Lernerfolge</li>
      <li>Zeitgemäße Medienkompetenzen</li>
    </ul>
  </section>

  <section class="section" style="top:386px">
    <h2 class="section__heading">Die Quarvelo GmbH bietet:</h2>
    <ul class="section__list">
      <li>Unterstützung während der Antragsstellung</li>
      <li>Erfahrung mit Schulen</li>
      <li>Professionelle WLAN-Beratung<br>von Konzept bis zur Konfiguration</li>
    </ul>
  </section>

  <div class="service" style="top:207px">
    <div class="service__icon">
      <svg viewBox="0 0 36 36"><g fill="none" stroke="var(--accent-orange)" stroke-width="3.2" stroke-linecap="round"><path d="M5 14a18 18 0 0 1 26 0"/><path d="M10 19a11 11 0 0 1 16 0"/><path d="M14.5 24a5 5 0 0 1 7 0"/></g><circle cx="18" cy="29" r="2.4" fill="var(--accent-orange)"/></svg>
    </div>
    <div class="service__label">WLAN Lösungen</div>
  </div>

  <div class="service" style="top:277px">
    <div class="service__icon">
      <svg viewBox="0 0 36 36"><rect x="3" y="5" width="30" height="20" rx="1.5" fill="var(--accent-orange)"/><rect x="6" y="8" width="24" height="14" fill="#fff"/><rect x="14" y="25" width="8" height="4" fill="var(--accent-orange)"/><rect x="10" y="29" width="16" height="2" fill="var(--accent-orange)"/><rect x="23" y="24" width="9" height="8" rx="1" fill="var(--brand-blue)"/><path d="M25 24v-2.5a2.5 2.5 0 0 1 5 0V24" fill="none" stroke="var(--brand-blue)" stroke-width="1.5"/></svg>
    </div>
    <div class="service__label">IT Sicherheit</div>
  </div>

  <div class="service" style="top:348px">
    <div class="service__icon">
      <svg viewBox="0 0 36 36"><path d="M7 18a11 11 0 0 1 22 0" fill="none" stroke="var(--accent-orange)" stroke-width="2.6"/><rect x="4" y="16" width="5" height="9" rx="2" fill="var(--accent-orange)"/><rect x="27" y="16" width="5" height="9" rx="2" fill="var(--accent-orange)"/><path d="M29.5 25c0 4-4 6-9 6" fill="none" stroke="var(--accent-orange)" stroke-width="1.8"/><circle cx="26" cy="29" r="5" fill="var(--brand-blue)"/><path d="M24.5 27.5a1.5 1.5 0 1 1 2 1.4V30" fill="none" stroke="#fff" stroke-width="1.2"/><circle cx="26.5" cy="31.5" r=".7" fill="#fff"/></svg>
    </div>
    <div class="service__label">Support vom<br>Fachmann</div>
  </div>

  <svg class="photo" viewBox="0 0 570 385" role="img" aria-label="Foto: lachender Schüler am Tablet im Klassenzimmer">
    <defs>
      <linearGradient id="classroomTones" x1="0" y1="0" x2="1" y2="1">
        <stop offset="0" stop-color="#d9c4ad"/>
        <stop offset=".45" stop-color="#c7a88a"/>
        <stop offset=".75" stop-color="#3f5a86"/>
        <stop offset="1" stop-color="#e6d8c4"/>
      </linearGradient>
    </defs>
    <path d="M247 110C350 90 460 66 570 58V385H247Z" fill="url(#classroomTones)"/>
  </svg>

  <svg class="wave-bottom" viewBox="0 0 570 105" preserveAspectRatio="none">
    <path d="M0 105C200 90 380 50 570 12V105Z" fill="var(--wave-light)"/>
    <path d="M120 105C300 88 450 58 570 40V105Z" fill="var(--wave-mid)"/>
    <path d="M260 105C400 92 500 78 570 68V105Z" fill="var(--brand-blue)"/>
  </svg>

  <aside class="benefits" style="top:511px;height:285px">
    <h3 class="benefits__heading">Ihre Vorteile auf einen Blick:</h3>
    <ul class="benefits__list" style="margin-top:2px">
      <li>Integration von modernen Lernmethoden</li>
      <li>Ständig verfügbare, digitale Lernumgebungen</li>
      <li>Digitale Kommunikationswege zwischen Lehrern und Schülern</li>
      <li>Direktes Feedback für Schüler und Lehrer</li>
      <li>Einbindung von BYOD-Konzepten und Screencasting</li>
      <li>Remote-Zugriff auf den Unterricht von Zuhause</li>
    </ul>
  </aside>

  <div class="contact">info@quarvelo-netz.de | www.quarvelo-netz.de</div>
</article>

</body>
</html>
```